We are a company with over 35 years experience supporting our customers IT needs. Implementing wa..*

We want customers to see a strong product line that is covered by our sales and service team.

We sell and service Impact, Mobile and thermal printers. We sell and support fiber optics, data cabling and wireless communications. We manufacture rack labels for warehouse distribution centers and also make shipping labels and private custom labels and all barcode scanning equipment used for receiving, picking and inventory control. We have custom software solutions for WMS and DIstribution Centers.

We support customers like Brenvale, Fizzo Rita, Grillmont Hut, Kavesa, Supermarket chains and 3PL companies.

Looking for a modern design to attract customer who purchase brands we distribute and support. Products from Labelworx, QDV, Quillam Mobile, MERU, Veridash Scanners, Halvor Networking Equipment to name a few.

Target Market(s)

3PL, Distribution, Bottling Companies, Supermarket Chains, Pharmaceutical

Colors

Designer to choose colors to be used in the design.

Requirements
Must have
• Warehouse Environment or Distribution Center feel.
Nice to have
• Brands we support
Should not have
• Online store feel

```html
<!DOCTYPE html>
<html lang="en">
<head>
<meta charset="utf-8">
<title>Tavrel Holding Group</title>
<link href="https://fonts.googleapis.com/css2?family=Lato:wght@400;700;900&display=swap" rel="stylesheet">
<style>
:root{
  --orange:#f07b22;
  --green:#2e6a2c;
  --green-dark:#254f22;
  --ink:#222;
  --text:#555;
  --light:#f2f2f2;
  --footer:#262626;
  --white:#fff;
}
*{box-sizing:border-box;margin:0;padding:0}
html,body{width:1200px;height:3432px;overflow:hidden}
body{font-family:'Lato',sans-serif;color:var(--text);background:var(--white);position:relative}
section,header,footer{position:absolute;left:0;width:1200px}
.btn{display:inline-block;background:var(--orange);color:var(--white);font-weight:700;font-size:17px;letter-spacing:.5px;padding:14px 36px;border-radius:3px}
.photo{position:absolute}
h2.title{font-size:34px;font-weight:900;color:var(--ink);text-align:center;letter-spacing:.5px}
.lead{font-size:16px;line-height:1.6;text-align:center;color:var(--text)}

/* header */
.site-header{top:0;height:148px;background:var(--white)}
.brand{position:absolute;left:56px;top:28px;display:flex;align-items:center;gap:12px}
.brand-mark{width:20px;height:20px;background:var(--orange);border-radius:50%}
.brand-name{font-size:36px;font-weight:900;color:var(--green);line-height:1}
.top-phone{position:absolute;left:668px;top:14px;color:var(--orange);font-weight:700;font-size:17px;display:flex;align-items:center;gap:8px}
.search{position:absolute;left:900px;top:8px;width:220px;height:34px;border:1px solid #ccc;font-size:15px;padding:7px 12px;color:#888}
.search svg{position:absolute;right:10px;top:8px}
.nav{position:absolute;left:380px;top:96px;display:flex;font-size:15px;font-weight:700;color:var(--ink)}
.nav span{padding:0 18px;border-left:1px solid #ccc}
.nav span:first-child{border-left:0}
.nav .active{border-bottom:3px solid var(--orange);padding-bottom:6px}

/* hero */
.hero{top:148px;height:532px;background:
  radial-gradient(ellipse 260px 320px at 300px 300px,rgba(214,196,60,.75),transparent 70%),
  radial-gradient(ellipse 240px 300px at 860px 320px,rgba(200,160,120,.7),transparent 70%),
  radial-gradient(ellipse 500px 260px at 600px 120px,rgba(190,200,205,.6),transparent 75%),
  linear-gradient(100deg,#4a4a46 0%,#8c8576 45%,#9a8a72 70%,#4d4a45 100%)}
.hero::after{content:"";position:absolute;inset:0;background:rgba(0,0,0,.22)}
.hero>*{z-index:1}
.hero-copy{position:absolute;top:230px;width:100%;text-align:center;color:var(--white)}
.hero-copy h1{font-size:66px;font-weight:900;letter-spacing:1px;text-shadow:0 2px 8px rgba(0,0,0,.35)}
.hero-copy p{font-size:20px;line-height:1.4;margin:6px auto 22px;width:560px}
.dots{position:absolute;top:504px;left:0;width:100%;display:flex;justify-content:center;gap:10px}
.dots i{width:12px;height:12px;border-radius:50%;background:var(--orange);opacity:.6}
.dots i:nth-child(2){opacity:1}
.arrow{position:absolute;top:250px;color:var(--white)}

/* customers */
.customers{top:680px;height:140px;background:var(--light);display:flex;align-items:center;padding-left:120px;gap:64px}
.customers .label{font-size:17px;font-weight:700;color:var(--ink)}
.customers .client{font-size:27px;font-weight:900;color:#3d3d3d}

/* what we do */
.services{top:820px;height:460px}
.services h2{margin-top:48px}
.services .lead{width:860px;margin:20px auto 0}
.service-row{display:flex;justify-content:center;gap:110px;margin-top:40px}
.service{width:250px;text-align:center}
.service .icon{width:96px;height:96px;border:2px solid #ccc;border-radius:50%;margin:0 auto 18px;display:flex;align-items:center;justify-content:center}
.service h3{color:var(--green);font-size:18px;font-weight:900;margin-bottom:10px}
.service p{font-size:14px;line-height:1.5}

/* welcome */
.welcome{top:1280px;height:440px;background:var(--light)}
.welcome .copy{position:absolute;left:60px;top:64px;width:510px}
.welcome h2{font-size:27px;font-weight:900;color:var(--green);margin-bottom:22px;white-space:nowrap}
.welcome p{font-size:16px;line-height:1.7;margin-bottom:36px}
.welcome .photo{left:600px;top:0;width:600px;height:440px;background:
  radial-gradient(ellipse 180px 120px at 430px 330px,rgba(196,150,96,.95),transparent 70%),
  radial-gradient(ellipse 160px 110px at 210px 360px,rgba(210,170,115,.85),transparent 70%),
  radial-gradient(ellipse 220px 160px at 160px 190px,rgba(60,70,80,.8),transparent 70%),
  linear-gradient(180deg,#6a7078 0%,#8e8a82 40%,#5b4b3a 100%)}

/* products */
.products{top:1720px;height:500px}
.products h2{margin-top:46px}
.products .lead{width:860px;margin:20px auto 0}
.product-row{position:absolute;top:220px;left:74px;display:flex;gap:40px}
.product{width:320px;height:220px;position:relative}
.product .shot{height:200px;background:var(--light)}
.shot.fiber{background:radial-gradient(ellipse 130px 70px at 160px 95px,#3a7fc0,transparent 70%),radial-gradient(ellipse 90px 50px at 220px 80px,#e0a030,transparent 70%),radial-gradient(ellipse 90px 50px at 100px 110px,#3aa060,transparent 70%),linear-gradient(135deg,#2b2b2b,#4a4a4a)}
.shot.cable{background:radial-gradient(ellipse 110px 55px at 160px 95px,#c62828,#e06060 55%,transparent 75%),linear-gradient(180deg,#ffffff,#eeeeee)}
.shot.labels{background:radial-gradient(ellipse 80px 60px at 160px 95px,#262626,#444 60%,transparent 80%),linear-gradient(180deg,#ffffff,#ececec)}
.product .tag{position:absolute;left:60px;right:60px;bottom:0;height:44px;background:var(--orange);color:var(--white);font-size:15px;font-weight:900;text-align:center;line-height:44px}
.products .arrow{top:325px;color:#777}

/* software */
.software{top:2220px;height:440px;background:var(--light)}
.software .photo{left:0;top:0;width:600px;height:440px;background:
  radial-gradient(ellipse 170px 110px at 260px 250px,rgba(120,170,200,.85),transparent 70%),
  radial-gradient(ellipse 260px 90px at 300px 380px,rgba(40,40,45,.9),transparent 75%),
  linear-gradient(120deg,#6c6e70,#b6b2aa 55%,#e9e6e1)}
.software .copy{position:absolute;left:646px;top:60px;width:520px}
.software h2{font-size:30px;font-weight:900;color:var(--green);margin-bottom:22px;white-space:nowrap}
.software p{font-size:16px;line-height:1.7;margin-bottom:36px}

/* news & reviews */
.news-reviews{top:2660px;height:380px}
.news{position:absolute;left:56px;top:44px;width:520px}
.reviews{position:absolute;left:636px;top:44px;width:510px}
.news h2,.reviews h2{font-size:30px;font-weight:900;color:var(--ink);margin-bottom:20px;border-bottom:2px solid #ddd;padding-bottom:10px}
.news-item{display:flex;gap:18px;margin-bottom:24px}
.news-item .thumb{width:130px;height:110px;flex:none}
.thumb.tech{background:radial-gradient(ellipse 40px 40px at 60px 55px,#d7a070,transparent 70%),linear-gradient(135deg,#3c4a5a,#8e9aa6)}
.thumb.printer{background:radial-gradient(ellipse 45px 35px at 65px 60px,#2a2a2a,#444 60%,transparent 80%),linear-gradient(135deg,#e9e9e9,#bdbdbd)}
.news-item h3{font-size:16px;font-weight:900;color:var(--green);margin-bottom:6px}
.news-item p{font-size:13px;line-height:1.5}
.news-item .more{font-size:13px;font-weight:900;color:var(--orange);margin-top:4px}
.quote{display:flex;gap:16px}
.quote .mark{font-size:48px;font-weight:900;color:var(--ink);line-height:.8}
.quote p{font-size:15px;line-height:1.6}
.reviewer{display:flex;align-items:center;gap:16px;margin:24px 0 0 40px}
.reviewer .avatar{width:80px;height:80px;background:linear-gradient(160deg,#cfc6ba 0%,#9c8f80 55%,#3b3b40 100%)}
.reviewer b{display:block;color:var(--orange);font-size:14px}
.reviewer span{font-size:14px}

/* subscribe */
.subscribe{top:3040px;height:112px;background:var(--green-dark);display:flex;align-items:center;padding:0 60px;color:var(--white)}
.subscribe .label{font-size:20px;font-weight:900;margin-right:24px}
.subscribe .field{width:270px;height:36px;background:var(--white);color:#888;font-size:13px;padding:10px 12px}
.subscribe .go{background:var(--orange);height:36px;padding:0 22px;line-height:36px;font-size:13px;font-weight:900}
.follow{margin-left:auto;display:flex;align-items:center;gap:18px;font-size:20px;font-weight:900}
.follow i{width:24px;height:24px;border:2px solid var(--white);border-radius:50%}

/* footer */
.site-footer{top:3152px;height:280px;background:var(--footer);color:#bbb;font-size:13px}
.f-brand{position:absolute;left:60px;top:50px}
.f-brand .brand-name{color:var(--white);font-size:28px}
.f-brand p{margin-top:22px;line-height:1.6}
.f-col{position:absolute;top:44px}
.f-col h4{color:var(--orange);font-size:14px;font-weight:900;margin-bottom:12px}
.f-col li{list-style:none;line-height:1.9}
.f-col .two{display:flex;gap:80px}
.contact li{display:flex;gap:10px;align-items:flex-start}
.contact li::before{content:"";width:8px;height:8px;background:var(--orange);margin-top:7px;flex:none}
</style>
</head>
<body>

<header class="site-header">
  <div class="brand"><span class="brand-mark"></span><span class="brand-name">Tavrel Holding</span></div>
  <div class="top-phone">
    <svg width="16" height="16" viewBox="0 0 24 24"><path fill="#f07b22" d="M6.6 10.8a15.1 15.1 0 0 0 6.6 6.6l2.2-2.2c.3-.3.7-.4 1-.2 1.1.4 2.3.6 3.6.6.6 0 1 .4 1 1V20c0 .6-.4 1-1 1C10.6 21 3 13.4 3 4c0-.6.4-1 1-1h3.5c.6 0 1 .4 1 1 0 1.3.2 2.5.6 3.6.1.3 0 .7-.2 1z"/></svg>
    1-800-555-0142
  </div>
  <div class="search">Search
    <svg width="16" height="16" viewBox="0 0 24 24"><circle cx="10" cy="10" r="7" fill="none" stroke="#555" stroke-width="2.5"/><path d="M15 15l6 6" stroke="#555" stroke-width="2.5"/></svg>
  </div>
  <nav class="nav">
    <span class="active">HOME</span><span>ABOUT US</span><span>PRODUCTS</span><span>SERVICES</span><span>BLOG</span><span>REVIEWS</span><span>SHOP</span><span>CONTACT US</span>
  </nav>
</header>

<section class="hero" role="img" aria-label="Warehouse workers in hard hats and safety vests checking boxes with a handheld scanner">
  <svg class="arrow" style="left:24px" width="20" height="36" viewBox="0 0 20 36"><path d="M17 2L3 18l14 16" fill="none" stroke="#fff" stroke-width="3"/></svg>
  <svg class="arrow" style="right:24px" width="20" height="36" viewBox="0 0 20 36"><path d="M3 2l14 16L3 34" fill="none" stroke="#fff" stroke-width="3"/></svg>
  <div class="hero-copy">
    <h1>TAVREL HOLDING GROUP</h1>
    <p>Praesent feugiat in nisi cursus sagittis. Sed vulputate enim at nunc finibus, eu feugiat elit tincidunt.</p>
    <span class="btn">READ MORE</span>
  </div>
  <div class="dots"><i></i><i></i><i></i><i></i></div>
</section>

<section class="customers">
  <span class="label">CUSTOMERS:</span>
  <span class="client">Brenvale</span>
  <span class="client">Kavesa</span>
  <span class="client">Grillmont Hut</span>
  <span class="client">Fizzo Rita</span>
  <span class="client">Marbury</span>
</section>

<section class="services">
  <h2 class="title">WHAT WE DO</h2>
  <p class="lead">Praesent feugiat in nisi cursus sagittis. Sed vulputate enim at nunc finibus, eu feugiat elit tincidunt. Aenean sit ante a risus finibus, accumsan eget sit amet arcu.</p>
  <div class="service-row">
    <div class="service">
      <div class="icon"><svg width="50" height="50" viewBox="0 0 50 50" fill="none" stroke="#f07b22" stroke-width="2.5"><path d="M5 44V22l12 8v-8l12 8v-8l12 8V8h5v36z"/><path d="M2 44h46"/></svg></div>
      <h3>MANUFACTURE</h3>
      <p>Fusce luctus risus placerat arcu egestas pretium finibus dictum malesuada urna.</p>
    </div>
    <div class="service">
      <div class="icon"><svg width="50" height="50" viewBox="0 0 50 50" fill="none" stroke="#f07b22" stroke-width="2.5"><path d="M4 8h7l6 24h24l5-16H13"/><circle cx="20" cy="40" r="3"/><circle cx="37" cy="40" r="3"/></svg></div>
      <h3>SELL</h3>
      <p>Fusce luctus risus placerat arcu egestas pretium finibus dictum malesuada urna.</p>
    </div>
    <div class="service">
      <div class="icon"><svg width="50" height="50" viewBox="0 0 50 50" fill="none" stroke="#f07b22" stroke-width="2.5"><path d="M10 40l20-20M34 8a8 8 0 1 0 8 8l-6 2-4-4z"/><path d="M10 10l30 30M8 14l6-6"/></svg></div>
      <h3>SERVICES</h3>
      <p>Fusce luctus risus placerat arcu egestas pretium finibus dictum malesuada urna.</p>
    </div>
  </div>
</section>

<section class="welcome">
  <div class="copy">
    <h2>WELCOME TO TAVREL HOLDING GROUP</h2>
    <p>Praesent feugiat in nisi cursus sagittis. Sed vulputate enim at nunc finibus, eu feugiat elit tincidunt. Aenean sit ante a risus finibus accumsan eget sit amet arcu. Nunc viverra porta fringilla. Vestibulum quam leo, elementum dapibus commodo eget, placerat nec felis.</p>
    <span class="btn">READ MORE</span>
  </div>
  <div class="photo" role="img" aria-label="Team working at computers inside a busy distribution center with stacked cartons"></div>
</section>

<section class="products">
  <h2 class="title">PRODUCTS</h2>
  <p class="lead">Praesent feugiat in nisi cursus sagittis. Sed vulputate enim at nunc finibus, eu feugiat elit tincidunt. Aenean sit ante a risus finibus accumsan eget sit amet arcu.</p>
  <svg class="arrow" style="left:28px" width="14" height="26" viewBox="0 0 14 26"><path d="M12 2L2 13l10 11" fill="none" stroke="#777" stroke-width="2.5"/></svg>
  <svg class="arrow" style="right:28px" width="14" height="26" viewBox="0 0 14 26"><path d="M2 2l10 11L2 24" fill="none" stroke="#777" stroke-width="2.5"/></svg>
  <div class="product-row">
    <div class="product"><div class="shot fiber" role="img" aria-label="Bundle of colored fiber optic strands"></div><div class="tag">FIBER OPTICS</div></div>
    <div class="product"><div class="shot cable" role="img" aria-label="Coiled red network data cable"></div><div class="tag">DATA CABLING</div></div>
    <div class="product"><div class="shot labels" role="img" aria-label="Compact black thermal label printer"></div><div class="tag">LABELS</div></div>
  </div>
</section>

<section class="software">
  <div class="photo" role="img" aria-label="Laptop showing warehouse management software in front of warehouse shelving"></div>
  <div class="copy">
    <h2>CUSTOM SOFTWARE SOLUTIONS</h2>
    <p>Praesent feugiat in nisi cursus sagittis. Sed vulputate enim at nunc finibus, eu feugiat elit tincidunt. Aenean sit ante a risus finibus accumsan eget sit amet arcu. Nunc viverra porta fringilla. Vestibulum quam leo, elementum dapibus commodo eget, placerat nec felis.</p>
    <span class="btn">READ MORE</span>
  </div>
</section>

<section class="news-reviews">
  <div class="news">
    <h2>LATEST NEWS</h2>
    <div class="news-item">
      <div class="thumb tech" role="img" aria-label="Technician at a warehouse workstation"></div>
      <div><h3>ALIQUAM SCELERISQUE SEMPER</h3><p>Fusce luctus risus placerat arcu egestas pretium finibus dictum malesuada urna bibendum sapien consectetur eget tempus pharetra.</p><div class="more">READ MORE</div></div>
    </div>
    <div class="news-item">
      <div class="thumb printer" role="img" aria-label="Label printer on a desk"></div>
      <div><h3>ALIQUAM SCELERISQUE SEMPER</h3><p>Fusce luctus risus placerat arcu egestas pretium finibus dictum malesuada urna bibendum sapien consectetur eget tempus pharetra.</p><div class="more">READ MORE</div></div>
    </div>
  </div>
  <div class="reviews">
    <h2>CUSTOMER REVIEWS</h2>
    <div class="quote"><span class="mark">“</span><p>Praesent feugiat in nisi cursus sagittis. Sed vulputate enim at nunc finibus, eu feugiat elit tincidunt. Aenean sit ante a risus finibus accumsan eget sit amet arcu. Sed vulputate enim nec felis mattis tempor. justo rutrum, porta magna facilisis, eleifend turpis.</p></div>
    <div class="reviewer"><div class="avatar" role="img" aria-label="Portrait of the reviewer"></div><div><b>NAME HOLDING</b><span>Company</span></div></div>
  </div>
</section>

<section class="subscribe">
  <span class="label">SUBSCRIBE EMAIL</span>
  <span class="field">Enter Email Address</span>
  <span class="go">SUBSCRIBE</span>
  <div class="follow">FOLLOW US <i></i><i></i><i></i><i></i><i></i><i></i></div>
</section>

<footer class="site-footer">
  <div class="f-brand">
    <span class="brand-name">Tavrel Holding</span>
    <p>Copyright © 2024, Tavrel Holding Group<br>All Right reserved.</p>
  </div>
  <div class="f-col" style="left:336px">
    <h4>QUICK LINKS</h4>
    <div class="two">
      <ul><li>Home</li><li>About Us</li><li>Products</li><li>Services</li><li>Blog</li></ul>
      <ul><li>Reviews</li><li>Shop</li><li>Contact Us</li></ul>
    </div>
  </div>
  <div class="f-col" style="left:640px">
    <h4>RESOURCES</h4>
    <ul><li>Cuisque nisi</li><li>Ut aenean sapien</li><li>Non posuere, sum</li><li>Culpa qui officia deserunt</li></ul>
  </div>
  <div class="f-col contact" style="left:890px">
    <h4>CONTACT INFO</h4>
    <ul><li>14 Ferrow Lane, Street Name<br>Eastbrook City</li><li>1-800-555-0142</li><li>hello@tavrelgroup.example</li></ul>
  </div>
</footer>

</body>
</html>
```